Business card and company logo design needed

Need a business card and company logo design for all stationary for an Aviation refueling consultancy business. Our business offers consulting services in the specialist aviation refueling industry. Services range from engineering, compliance and management consultancy through to project management services. This encompasses infrastructure from refinery through to airport and into the aircraft wing.

Design should be simple, 'less-is-more' concept, possibly taking advantage of the 'm' for tevlon and the fact is it the aviation industry. It should convey confidence, safety, experience, professionalism, aviation, engineering?, and should not be afraid to be simple in color...though please do not let this restrict your designs and imagination.

Target Market(s)

Airport authorities, oil majors, aircraft operators

Industry/Entity Type

Airport

Contact Information for Business Card

Tevlon Skyward Advisory Pty Ltd
Darius Tevlon
Director
mobile:+61427305158
email: darius@tevlonadvisory.example
Skype: darius.tevlonadvisory

Logo styles of interest
Emblem Logo
Pictorial/Combination Logo
Abstract Logo
Wordmark Logo
Lettermark Logo
Requirements
Must have
• - A feel of safety, security and confidence
Nice to have
• - Aviation has both heritage and modern 'sexy' elements so would be nice to try and capture both
- Aviation 'JET' fuel color is designated as black in signage or labels
- Themes? : Aviation fuel is derived from oil, it burns, safety, Jet fuel is colorless
- Company is global in reach, borderless like aircraft
Should not have
• - Cliche:

```html
<!DOCTYPE html>
<html lang="en">
<head>
<meta charset="utf-8">
<title>Tevlon Skyward Advisory – Business Card</title>
<link rel="stylesheet" href="https://fonts.googleapis.com/css2?family=Questrial&display=swap">
<style>
  :root {
    --page-bg: #ffffff;
    --leaf-green: #62dc00;
    --lime-band: #84ff00;
    --outer-band: #aaff22;
    --trail-green: #d2ff8a;
    --plane-tint: #9fe86a;
    --text-green: #5fd000;
    --logo-text: #c6ff5a;
  }
  html, body {
    margin: 0;
    padding: 0;
    width: 1200px;
    height: 1000px;
    overflow: hidden;
    background: var(--page-bg);
  }
  .canvas {
    position: relative;
    width: 1200px;
    height: 1000px;
    font-family: "Questrial", "Century Gothic", sans-serif;
  }
  .card-art {
    position: absolute;
    left: 0;
    top: 0;
  }
  .company-name {
    position: absolute;
    left: 205px;
    top: 468px;
    margin: 0;
    font-size: 15px;
    font-weight: 400;
    color: var(--logo-text);
    letter-spacing: 0.2px;
    display: flex;
    align-items: center;
    gap: 10px;
  }
  .company-name .mark-dot {
    width: 14px;
    height: 14px;
    border-radius: 50%;
    background: var(--logo-text);
  }
  .contact {
    position: absolute;
    left: 640px;
    top: 385px;
    color: var(--text-green);
  }
  .contact .person {
    margin: 0 0 66px;
    font-size: 32px;
    font-weight: 400;
  }
  .contact .line {
    margin: 0 0 26px;
    font-size: 18px;
  }
</style>
</head>
<body>
<main class="canvas">
  <svg class="card-art" width="1200" height="1000" viewBox="0 0 1200 1000" aria-hidden="false">
    <!-- outer lime band -->
    <path d="M180 270 H540 C700 410 700 640 520 730 H180 Q150 730 150 700 V300 Q150 270 180 270 Z" fill="var(--outer-band)"/>
    <!-- middle lime band -->
    <path d="M180 270 H505 C650 410 650 630 490 730 H180 Q150 730 150 700 V300 Q150 270 180 270 Z" fill="var(--lime-band)"/>
    <!-- main green panel -->
    <path d="M180 270 H470 C600 410 600 620 455 730 H180 Q150 730 150 700 V300 Q150 270 180 270 Z" fill="var(--leaf-green)"/>
    <!-- flight trail -->
    <path d="M455 720 C560 560 700 440 900 330" fill="none" stroke="var(--trail-green)" stroke-width="5" stroke-linecap="round" opacity="0.9"/>
    <!-- aircraft silhouette area -->
    <rect x="880" y="282" width="110" height="70" rx="30" fill="var(--plane-tint)" role="img" aria-label="Jet aircraft silhouette climbing at the end of the flight trail"/>
  </svg>

  <p class="company-name"><span class="mark-dot"></span>Tevlon Skyward Advisory Pty Ltd</p>

  <section class="contact">
    <h1 class="person">Darius Tevlon Director</h1>
    <p class="line">mobile:+61427305158</p>
    <p class="line">email: darius@tevlonadvisory.example</p>
    <p class="line">Skype: darius.tevlonadvisory</p>
  </section>
</main>
</body>
</html>
```